New company looking for logo, for business cards and email signature.
we provide Safety, Training and Project Management Services to Mining and Transport sectors.

HALVORN CONSULTANCY, Tom Ashcrove, Principal Consultant, 0491362817, halvornconsultancy@postvale.example , Unit 412,KestwickRidge Business Hub,817 Tulloch Road, Mackay, 4832.
Sustainable Production through Safety, Training and Leadership.

```html
<!DOCTYPE html>
<html lang="en">
<head>
<meta charset="utf-8">
<title>Halvorn Consultancy – Business Card</title>
<link rel="stylesheet" href="https://fonts.googleapis.com/css2?family=Michroma&family=Oswald:wght@600&family=Open+Sans:wght@400;600&display=swap">
<style>
  :root {
    --stage: #d9d9d9;
    --card-black: #141414;
    --card-black-deep: #050505;
    --paper: #ffffff;
    --orange: #e07b1a;
    --orange-deep: #b95a0c;
    --silver: #d6d6d6;
    --ink: #111111;
    --muted: #e9e9e9;
    --divider: #6a6a6a;
  }
  * { box-sizing: border-box; margin: 0; padding: 0; }
  html, body { width: 1200px; height: 900px; overflow: hidden; }
  body {
    background: var(--stage);
    display: flex;
    align-items: center;
    justify-content: center;
    gap: 40px;
    font-family: "Open Sans", sans-serif;
  }
  .card {
    position: relative;
    width: 540px;
    height: 330px;
    border-radius: 22px;
    overflow: hidden;
    box-shadow: 0 10px 24px rgba(0,0,0,0.25);
  }

  /* Front */
  .card--front {
    background: radial-gradient(ellipse at 50% 40%, var(--card-black) 0%, var(--card-black-deep) 100%);
    display: flex;
    flex-direction: column;
    align-items: center;
    justify-content: center;
    gap: 26px;
  }
  .brand-mark {
    width: 86px;
    height: 86px;
    background: var(--orange);
  }
  .brand-wordmark {
    font-family: "Michroma", sans-serif;
    font-size: 24px;
    letter-spacing: 1px;
    color: var(--silver);
    white-space: nowrap;
  }

  /* Back */
  .card--back { background: var(--paper); }
  .back-header {
    position: absolute;
    left: 0; right: 0; top: 0;
    height: 172px;
    display: flex;
    flex-direction: column;
    align-items: center;
    padding-top: 26px;
    padding-left: 90px;
  }
  .back-header .brand-mark { width: 78px; height: 78px; }
  .back-header .brand-wordmark {
    color: var(--ink);
    font-size: 20px;
    margin-top: 22px;
  }
  .tagline-band {
    position: absolute;
    left: 0; right: 0; top: 176px;
    height: 20px;
    background: linear-gradient(90deg, var(--orange-deep), var(--orange) 40%, var(--orange));
    font-family: "Oswald", sans-serif;
    font-weight: 600;
    font-size: 12.5px;
    letter-spacing: 1.6px;
    color: var(--ink);
    text-transform: uppercase;
    line-height: 20px;
    text-align: center;
    white-space: nowrap;
  }
  .back-footer {
    position: absolute;
    left: 0; right: 0; top: 196px; bottom: 0;
    background: radial-gradient(ellipse at 50% 30%, var(--card-black) 0%, var(--card-black-deep) 100%);
    display: flex;
    align-items: center;
  }
  .person {
    width: 262px;
    text-align: right;
    padding-right: 18px;
  }
  .person__name {
    color: var(--orange);
    font-size: 19px;
    font-weight: 600;
  }
  .person__role {
    color: var(--muted);
    font-size: 13px;
    margin-top: 2px;
  }
  .divider {
    width: 1px;
    height: 96px;
    background: var(--divider);
  }
  .contacts {
    list-style: none;
    padding-left: 16px;
    color: var(--muted);
    font-size: 11.5px;
    line-height: 17px;
  }
  .contacts li { display: flex; align-items: flex-start; gap: 5px; }
  .contacts svg { width: 12px; height: 12px; margin-top: 2px; flex: none; fill: var(--orange); }
  .contacts .indent { padding-left: 17px; }
</style>
</head>
<body>

  <section class="card card--front">
    <div class="brand-mark"></div>
    <div class="brand-wordmark">HALVORN CONSULTANCY</div>
  </section>

  <section class="card card--back">
    <header class="back-header">
      <div class="brand-mark"></div>
      <div class="brand-wordmark">HALVORN CONSULTANCY</div>
    </header>
    <div class="tagline-band">Sustainable Production through Safety, Training and Leadership</div>
    <div class="back-footer">
      <div class="person">
        <div class="person__name">Tom Ashcrove</div>
        <div class="person__role">Principal Consultant</div>
      </div>
      <div class="divider"></div>
      <ul class="contacts">
        <li>
          <svg viewBox="0 0 24 24" aria-hidden="true"><path d="M6.6 10.8a15.1 15.1 0 0 0 6.6 6.6l2.2-2.2c.3-.3.7-.4 1-.2 1.1.4 2.3.6 3.6.6.6 0 1 .4 1 1V20c0 .6-.4 1-1 1A17 17 0 0 1 3 4c0-.6.4-1 1-1h3.5c.6 0 1 .4 1 1 0 1.3.2 2.5.6 3.6.1.3 0 .7-.2 1z"/></svg>
          0491362817
        </li>
        <li>
          <svg viewBox="0 0 24 24" aria-hidden="true"><path d="M2 5h20v14H2zm2 2v.5l8 5 8-5V7zm0 2.8V17h16V9.8l-8 5z"/></svg>
          halvornconsultancy@postvale.example
        </li>
        <li>
          <svg viewBox="0 0 24 24" aria-hidden="true"><path d="M12 3 2 12h3v8h5v-5h4v5h5v-8h3z"/></svg>
          Unit 412,KestwickRidge
        </li>
        <li class="indent">Business Hub,817 Tulloch Road</li>
        <li class="indent">Mackay, 4832</li>
      </ul>
    </div>
  </section>

</body>
</html>
```